Business card design and logo needed - Photographer

I take photos of weddings, rodeos, snowmobiling.
Need a card to hand out to prospective clients.
Industry/Entity Type
Business
Contact Information for Business Card
Marcus Dolven Photography
Requirements
Must have
- Bold
Black or white base.
My website. www.MarcusDolven.example
Should not have
- camera/ lens/ aperture blades

```html
<!DOCTYPE html>
<html lang="en">
<head>
<meta charset="utf-8">
<title>Marcus Dolven Photography – Business Card</title>
<link rel="stylesheet" href="https://fonts.googleapis.com/css2?family=Josefin+Sans:wght@400;600&display=swap">
<style>
  :root {
    --backdrop: #3b322d;
    --card-base: #1c1c1d;
    --card-edge: #141415;
    --spot-light: rgba(255, 255, 255, 0.22);
    --spot-soft: rgba(255, 255, 255, 0.05);
    --brand-text: #e8ecee;
    --pill-top: #3a3b3d;
    --pill-bottom: #1b1b1c;
    --pill-text: #f2f2f2;
    --mark-stroke: #8fc3cf;
  }
  html, body {
    margin: 0;
    width: 1200px;
    height: 716px;
    overflow: hidden;
    background: var(--backdrop);
  }
  .canvas {
    position: relative;
    width: 1200px;
    height: 716px;
    display: flex;
    align-items: center;
    justify-content: center;
  }
  .business-card {
    position: relative;
    width: 1000px;
    height: 572px;
    border-radius: 6px;
    background:
      radial-gradient(ellipse 260px 200px at 50% 4%, var(--spot-light), var(--spot-soft) 55%, transparent 80%),
      linear-gradient(180deg, var(--card-base), var(--card-edge));
    box-shadow: 0 18px 40px rgba(0, 0, 0, 0.45);
    overflow: hidden;
    font-family: "Josefin Sans", sans-serif;
  }
  .spotlight-lamp {
    position: absolute;
    top: 0;
    left: 50%;
    width: 150px;
    height: 4px;
    transform: translateX(-50%);
    border-radius: 0 0 50% 50%;
    background: rgba(255, 255, 255, 0.85);
    box-shadow: 0 0 24px 8px rgba(255, 255, 255, 0.35);
  }
  .brand {
    position: absolute;
    top: 176px;
    left: 0;
    right: 0;
    display: flex;
    flex-direction: column;
    align-items: center;
    gap: 22px;
  }
  .brand-dot {
    width: 54px;
    height: 54px;
    border-radius: 50%;
    border: 5px solid var(--mark-stroke);
    box-sizing: border-box;
  }
  .brand-name {
    margin: 0;
    color: var(--brand-text);
    font-weight: 600;
    font-size: 42px;
    letter-spacing: 8px;
    text-transform: uppercase;
    text-align: center;
    line-height: 1.25;
  }
  .website-pill {
    position: absolute;
    left: 50%;
    top: 440px;
    transform: translateX(-50%);
    width: 400px;
    height: 52px;
    border-radius: 8px;
    background: linear-gradient(180deg, var(--pill-top), var(--pill-bottom));
    box-shadow: inset 0 1px 0 rgba(255, 255, 255, 0.18), 0 4px 10px rgba(0, 0, 0, 0.5);
    display: flex;
    align-items: center;
    justify-content: center;
    color: var(--pill-text);
    font-size: 21px;
    letter-spacing: 2px;
  }
</style>
</head>
<body>
  <main class="canvas">
    <section class="business-card">
      <div class="spotlight-lamp"></div>
      <div class="brand">
        <div class="brand-dot"></div>
        <h1 class="brand-name">Marcus Dolven<br>Photography</h1>
      </div>
      <div class="website-pill">www.MarcusDolven.example</div>
    </section>
  </main>
</body>
</html>
```